Old boys day 2025

DURRAL KESTRELS V BELFORD HOUNDS SUNDAY 10TH AUGUST
THIS IS A FREE EVENT FOR FLOCK MEMBERS
THE FLOCK WOULD LIKE TO WELCOME ALL PAST PLAYERS,
COACHES, COMMITTEE, SPONSORS & SUPPORTERS TO OUR
ANNUAL KESTREL DAY OF CELEBRATION.
JOIN US IN THE FOUNDRY FOR A GREAT DAY OF LEAGUE ACTION
WATCHING OUR CURRENT CROP OF KESTRELS. YOU CAN PURCHASE A TICKET AND OR JOIN THE FLOCK @ WWW.DURRALFLOCK.EXAMPLE.AU
IF YOU JOIN THE FLOCK PRIOR TO THE EVENT OLD BOYS DAY IS FREE OF CHARGE, YOU STILL NEED TO
PURCHASE/REGISTER A TICKET ON THE EVENTS PAGE SO WE KNOW YOU ARE ATTENDING.
WE WILL BE HONOURING 6 PREMIERSHIP WINNING TEAMS THIS YEAR: 1935 1ST GRADE (90 YEARS), 1980 RESERVE GRADE (45 YEARS), 1985 1ST GRADE (40 YEARS), 1985 U18'S (40 YEARS), 2005 1ST GRADE (20 YEARS) & 2015 1ST GRADE (10 YEARS)
IN THE 1ST GRADE GAME THE PLAYERS WILL BE WEARING REPLICA 1985 JERSEYS (attached) WITH THE 85 PLAYERS NAMES ON THE BACK, THE FLOCK WILL BE HOSTING A POST GAME FUNCTION AT THE WREN LANE TAVERN WHERE THESE JERSEYS WILL BE AUCTIONED OFF TO RAISE MONEY.
PURCHASE YOUR TICKET AT WWW.DURRALFLOCK.EXAMPLE.AU/EVENTS

Target Market(s)

ex players

Requirements
Must have
• I NEED A A4 FLYER DESIGN & A DESIGN THAT WILL SUIT SOCIAL MEDIA

```html
<!DOCTYPE html>
<html lang="en">
<head>
<meta charset="utf-8">
<title>Old Boys Day Flyer – Durral Kestrels v Belford Hounds</title>
<link href="https://fonts.googleapis.com/css2?family=Open+Sans:wght@400;600;700&family=League+Gothic&family=Oswald:wght@400;500&family=Montserrat:wght@800&display=swap" rel="stylesheet">
<style>
:root{
  --page:#dcdde3;
  --sky:#29a8e0;
  --navy-ink:#2b2a7f;
  --navy:#1c2578;
  --royal:#2f4fc0;
  --night:#070b26;
  --grey-title:#b9b9bd;
  --red:#d7302a;
  --yellow:#f5e600;
  --pill:#2b2f92;
  --box-ink:#2b4aa0;
  --ticket:#2f7fd0;
  --white:#ffffff;
  --field:#3f8a2e;
}
*{margin:0;padding:0;box-sizing:border-box}
html,body{width:1200px;height:856px;overflow:hidden;background:var(--page)}
body{position:relative;font-family:"Open Sans",sans-serif}
.flyer{position:absolute;left:310px;top:18px;width:580px;height:820px;overflow:hidden;
  background:radial-gradient(ellipse 70% 50% at 50% 45%,var(--royal) 0%,var(--navy) 65%,#141a5c 100%);}
.stadium{position:absolute;left:0;top:372px;width:580px;height:380px;
  background:radial-gradient(ellipse 60% 45% at 50% 30%,#3d66c9 0%,#1a2c78 45%,var(--night) 100%);}
.field{position:absolute;left:0;bottom:0;width:580px;height:76px;
  background:linear-gradient(180deg,#0b1a12 0%,var(--field) 30%,#4d9a36 100%);}
.bowl{position:absolute;left:0;top:372px}
.top-band{position:absolute;left:0;top:0;width:580px;height:43px;background:var(--sky);
  color:var(--navy-ink);font-weight:700;font-size:18px;text-align:center;line-height:46px}
.club-mark{position:absolute;left:24px;top:64px;width:58px;height:62px;display:flex;flex-direction:column;align-items:center;justify-content:center;gap:5px}
.club-mark .dot{width:30px;height:30px;border-radius:50%;background:var(--white)}
.club-mark span{color:var(--white);font-weight:700;font-size:10px;white-space:nowrap}
.welcome{position:absolute;left:82px;top:62px;width:478px;text-align:center;color:var(--white);font-weight:700;font-size:14.5px;line-height:18.5px}
.title{position:absolute;left:0;width:580px;text-align:center;font-family:"League Gothic",sans-serif;font-weight:400}
.home{top:126px;font-size:84px;line-height:84px;color:var(--grey-title)}
.vs-row{position:absolute;left:0;top:206px;width:580px;height:48px;display:flex;align-items:center;justify-content:center;gap:34px}
.vs-row .v{font-family:"League Gothic",sans-serif;font-size:56px;color:var(--white);line-height:48px}
.team-tag{display:flex;flex-direction:column;align-items:center;gap:3px;width:64px;font-weight:700;font-size:9px}
.team-tag i{display:block;width:24px;height:24px;border-radius:50%}
.home-tag{color:var(--white)}
.home-tag i{background:var(--white)}
.away-tag{color:var(--red)}
.away-tag i{background:var(--red)}
.away{top:246px;font-size:84px;line-height:80px;color:var(--red)}
.date{top:316px;font-size:54px;line-height:52px;color:var(--white)}
.invite{position:absolute;left:0;top:380px;width:580px;text-align:center;font-weight:700;font-size:16.5px;line-height:21px;color:var(--white)}
.invite .lead{color:var(--sky)}
.ticket{position:absolute;left:30px;top:496px;width:180px;height:64px;transform:rotate(-9deg)}
.ticket .stub{position:absolute;left:0;top:0;width:140px;height:64px;background:var(--ticket);color:#123a8a;font-family:"Oswald",sans-serif;font-size:8.5px;line-height:11px;padding:13px 4px 0 4px;text-align:center;white-space:nowrap}
.ticket .tab{position:absolute;left:140px;top:0;width:40px;height:64px;background:var(--white);display:flex;flex-direction:column;align-items:center;justify-content:center;gap:4px;font-family:"Oswald",sans-serif;font-size:10px;color:#111}
.ticket .tab i{display:block;width:20px;height:20px;border-radius:50%;background:#1b1b1b}
.join-note{position:absolute;left:214px;top:472px;width:346px;text-align:center;color:var(--white);font-weight:700;font-size:16px;line-height:20.6px}
.honour{position:absolute;left:29px;top:588px;width:521px;height:40px;border-radius:20px;background:var(--pill);
  color:var(--yellow);font-family:"Montserrat",sans-serif;font-weight:800;font-size:14.5px;line-height:40px;text-align:center}
.jersey-card{position:absolute;left:0;top:636px;width:233px;height:112px;background:var(--white);border-radius:0 14px 14px 0}
.jersey-card p{position:absolute;left:18px;top:12px;width:112px;color:var(--box-ink);font-size:11.5px;line-height:14px}
.jersey-art{position:absolute;left:132px;top:6px;width:96px;height:100px;border-radius:8px;
  background:linear-gradient(160deg,#f2f2f2 0%,#d9d9d9 55%,#2a2a2a 100%)}
.teams{position:absolute;left:256px;top:637px;width:292px;border-collapse:collapse;color:var(--white);font-size:15px}
.teams td{height:18.6px;line-height:18px;padding:0}
.teams td:nth-child(1){width:70px}
.teams td:nth-child(3){text-align:right}
.footer{position:absolute;left:0;top:754px;width:580px;text-align:center;color:var(--white);font-size:13px;line-height:16px}
.footer strong{display:block;font-size:16.5px;line-height:22px;margin-top:1px}
</style>
</head>
<body>
<main class="flyer">
  <div class="stadium" role="img" aria-label="Night stadium stands with floodlights and sparkles"></div>
  <div class="field" role="img" aria-label="Green football field with yard markings"></div>
  <svg class="bowl" width="580" height="80" viewBox="0 0 580 80" aria-hidden="true">
    <path d="M0 8 Q290 120 580 8 L580 0 L0 0 Z" fill="#22339a"/>
    <path d="M0 8 Q290 120 580 8" fill="none" stroke="#5a86e0" stroke-width="2"/>
  </svg>

  <div class="top-band">This Is a Free Event for Flock Members</div>

  <div class="club-mark"><div class="dot"></div><span>THE FLOCK</span></div>
  <p class="welcome">The Flock Would Like to Welcome<br>All Past Players, Coaches, Committee, Sponsors &amp; Supporters<br>to our Annual Kestrel Day of Celebration.</p>

  <h1 class="title home">Durral Kestrels</h1>
  <div class="vs-row">
    <span class="team-tag home-tag"><i></i>DURRAL</span>
    <span class="v">V</span>
    <span class="team-tag away-tag"><i></i>BELFORD</span>
  </div>
  <h2 class="title away">Belford Hounds</h2>
  <p class="title date">Sunday 10th August</p>

  <p class="invite"><span class="lead">Join Us in The Foundry for a Great Day of League Action</span><br>Watching Our Current Crop of Kestrels.</p>

  <div class="ticket">
    <div class="stub">You can purchase a<br>Ticket and or Join<br>The Flock@www.durralflock.example.au</div>
    <div class="tab"><i></i>Ticket</div>
  </div>
  <p class="join-note">If You Join The Flock Prior to The Event<br>Old Boys Day is Free of Charge, You<br>Still need to Purchase/register a Ticket<br>on The Events Page so We Know you<br>are Attending.</p>

  <div class="honour">We will be Honouring 6 Premiership Winning Teams This Year:</div>

  <div class="jersey-card">
    <p>In the 1st Grade Game The Players will be wearing replica 1985 Jerseys with The 85 Players Names on the Back,</p>
    <div class="jersey-art" role="img" aria-label="Replica 1985 white and black club jersey"></div>
  </div>

  <table class="teams">
    <tr><td>1935</td><td>1st Grade</td><td>(90 Years)</td></tr>
    <tr><td>1980</td><td>Reserve Grade</td><td>(45 Years)</td></tr>
    <tr><td>1985</td><td>1st Grade</td><td>(40 Years)</td></tr>
    <tr><td>1985</td><td>U18's</td><td>(40 Years)</td></tr>
    <tr><td>2005</td><td>1st Grade</td><td>(20 Years)</td></tr>
    <tr><td>2015</td><td>1st Grade</td><td>(10 Years)</td></tr>
  </table>

  <p class="footer">The Flock Will Be Hosting a Post Game Function at the Wren Lane Tavern<br>where these Jerseys will be auctioned Off to Raise Money. Purchase Your Ticket At<strong>www.durralflock.example.au/events</strong></p>
</main>
</body>
</html>
```